Tides of the barrio "Las mareas del barrio nuevo"

I'm writing a book about word of mouth and the consumer as the media "the book is in Spanish" so you have to use "Las mareas del barrio nuevo" the subtitle is and 30 examples that proves it "Con doce relatos de esquina"

Book is about the power of consumer nowadays , the book will combine the era of social media but also the power of one to one word of mouth meaning w/o being connected to an electronic platform

Tides of the new barrio is a book about the power that now the consumer has in this double way interaction between the brands and the consumer, between the services and the people between the social media and the traditional media.

Consumer is on control and it is because "tides of the new barrio"

About book principles
I love simple books white background, simplicity around the fonts and the images (simple is better)

Target Market(s)

Marketing and digital marketing managers, social media managers, community managers, social media agencies, business people

Industry/Entity Type

Electronic

Requirements
Must have
• White backgroung, black and red fonts big fonts
Nice to have
• the subtitle "Con doce relatos de la calle"

```html
<!DOCTYPE html>
<html lang="es">
<head>
<meta charset="utf-8">
<title>Las mareas del barrio nuevo — cubierta</title>
<link rel="stylesheet" href="https://fonts.googleapis.com/css2?family=Josefin+Sans:wght@400;600;700&display=swap">
<style>
  :root {
    --page: #ececec;
    --paper: #ffffff;
    --ink: #111111;
    --accent-red: #c4161c;
    --edge: #d6d6d6;
    --sky-top: #8fb0e0;
    --sky-mid: #c9dcef;
    --cloud: #eef1f4;
    --rock: #8c8178;
    --box: #050505;
    --box-text: #ffffff;
  }
  * { box-sizing: border-box; margin: 0; padding: 0; }
  html, body { width: 1200px; height: 800px; overflow: hidden; }
  body {
    background: var(--page);
    font-family: "Josefin Sans", "Futura", sans-serif;
    color: var(--ink);
  }
  .cover-wrap {
    position: absolute;
    left: 185px; top: 90px;
    width: 830px; height: 620px;
    display: flex;
    border: 1px solid var(--edge);
    background: var(--paper);
  }
  .back-cover {
    width: 400px; height: 100%;
    background: var(--paper);
    position: relative;
    padding: 22px 24px 0;
  }
  .spine {
    width: 30px; height: 100%;
    background: var(--paper);
    border-left: 1px solid var(--edge);
    border-right: 1px solid var(--edge);
    writing-mode: vertical-rl;
    display: flex;
    justify-content: space-between;
    align-items: center;
    padding: 16px 0;
  }
  .spine-title { font-size: 17px; font-weight: 600; letter-spacing: 1.5px; text-transform: uppercase; color: var(--ink); }
  .spine-author { font-size: 9px; font-weight: 700; color: var(--accent-red); }
  .front-cover {
    width: 400px; height: 100%;
    position: relative; overflow: hidden;
    background: var(--paper);
    padding: 22px 24px 0;
  }
  .cover-photo {
    position: absolute; left: 0; right: 0; top: 290px; bottom: 0;
    background: linear-gradient(180deg, var(--sky-top) 0%, var(--sky-mid) 40%, var(--cloud) 65%, var(--rock) 100%);
  }
  .author-name {
    text-align: right; font-size: 13px; font-weight: 700;
    margin-right: 4px; margin-bottom: 4px;
  }
  .book-title {
    font-weight: 600; text-transform: uppercase; line-height: 0.9;
    color: var(--ink);
  }
  .title-line { display: block; white-space: nowrap; }
  .title-line.small { font-size: 27px; }
  .title-line .article { font-size: 22px; margin-right: 4px; color: var(--accent-red); }
  .title-line.huge { font-size: 82px; margin-top: 2px; }
  .subtitle {
    font-size: 16px; font-weight: 600; text-transform: uppercase;
    letter-spacing: 0.5px; margin-top: 12px;
    color: var(--accent-red);
  }
  .blurb {
    margin-top: 22px;
    font-size: 9.6px; line-height: 1.42; font-weight: 600;
    text-align: justify; text-align-last: center;
  }
  .back-footer {
    position: absolute; left: 24px; right: 24px; bottom: 22px;
    display: flex; justify-content: space-between;
  }
  .placeholder-box {
    width: 112px; height: 44px; background: var(--box);
    color: var(--box-text); font-size: 10px; font-weight: 600;
    display: flex; align-items: center; justify-content: center;
  }
</style>
</head>
<body>
  <main class="cover-wrap">
    <section class="back-cover">
      <p class="author-name">Author Name</p>
      <h2 class="book-title">
        <span class="title-line small"><span class="article">Las</span>Mareas del barrio</span>
        <span class="title-line huge">Nuevo</span>
      </h2>
      <p class="subtitle">Con doce relatos de esquina</p>
      <p class="blurb">Lorem ipsum dolor sit amet, consectetur adipisicing elit, sed do eiusmod tempor incididunt ut labore et dolore magna aliqua. Ut enim ad minim veniam, quis nostrud exercitation. Lorem ipsum dolor sit amet, consectetur adipisicing elit, sed do eiusmod tempor incididunt ut labore et dolore magna aliqua. Ut enim ad minim veniam, quis nostrud exercitation. Lorem ipsum dolor sit amet, consectetur adipisicing elit, sed do eiusmod tempor incididunt ut labore et dolore magna aliqua. Ut enim ad minim veniam, quis nostrud exercitation. Lorem ipsum dolor sit amet, consectetur adipisicing elit, sed do eiusmod tempor incididunt ut labore et dolore magna aliqua. Ut enim ad minim veniam, quis nostrud exercitation. Lorem ipsum dolor sit amet, consectetur adipisicing elit, sed do eiusmod tempor incididunt ut labore et dolore magna aliqua. Ut enim ad minim veniam, quis nostrud exercitation. Lorem ipsum dolor sit amet, consectetur adipisicing elit, sed do eiusmod tempor incididunt ut labore et dolore magna aliqua. Ut enim ad minim veniam, quis nostrud exercitation. Lorem ipsum dolor sit amet, consectetur adipisicing elit, sed do eiusmod tempor incididunt ut labore et dolore magna aliqua. Ut enim ad minim veniam, quis nostrud exercitation.</p>
      <div class="back-footer">
        <div class="placeholder-box">LOGO</div>
        <div class="placeholder-box">ISBN</div>
      </div>
    </section>

    <section class="spine">
      <span class="spine-title">Las mareas del barrio nuevo</span>
      <span class="spine-author">Author Name</span>
    </section>

    <section class="front-cover">
      <div class="cover-photo" role="img" aria-label="Fotografía: dos personas en traje tiran de una cuerda sobre una cumbre rocosa rodeada de nubes, bajo un cielo azul"></div>
      <p class="author-name">Author Name</p>
      <h1 class="book-title">
        <span class="title-line small"><span class="article">Las</span>Mareas del barrio</span>
        <span class="title-line huge">Nuevo</span>
      </h1>
      <p class="subtitle">Con doce relatos de esquina</p>
    </section>
  </main>
</body>
</html>
```